It is a leisure sector investment company.The company plans to invest in a luxurious 5 star resort

We need a stationery design to our company 'Solmaran Crest Limited' using the winning logo design. We need the letter heads, envelopes & the business cards. Should be simple, plain and professional
Updates
We have upload the source file & vector files which gives our logo design. We prefer the bottom logo.

Have updated under 'must have priorities', the company name, address, tel no. fax no. & the company reg no. which should come on the letter head. the long envelope should have the company name, tel & fax no. 
Business card should have the company name, name on the card, designation, tel no. fax no.  

Industry/Entity Type
Investment
Requirements
Must have
- Letter head details:
Solmaran Crest Limited
14 Floor, North Block, Harbour Meridian Plaza,
Velmont Circus, Colombo 01, Sri Lanka
Tel: +94 11 2764502 Fax: +94 11 2764508
Company Reg No.PB 6192
Long Envelope should have only the company name, adress, Tel & Fax
Business Cards should have the company name, Tel & Fax:
Business Card 1 - Lasantha Wijeratne - Chairman
Business Card 2 - Nuwan.S.Gunawardhana - COO

```html
<!DOCTYPE html>
<html lang="en">
<head>
<meta charset="utf-8">
<title>Solmaran Crest Limited – Business Cards</title>
<link rel="stylesheet" href="https://fonts.googleapis.com/css2?family=Arimo&family=Cinzel:wght@400&family=Cormorant+Garamond:ital,wght@1,400&display=swap">
<style>
  :root {
    --brand-brown: #5b4a42;
    --ink: #5a4a42;
    --band-light: #ffffff;
    --band-dark: #857a74;
    --watermark: #ececec;
    --paper: #ffffff;
  }
  html, body {
    margin: 0;
    padding: 0;
    overflow: hidden;
    background: var(--paper);
  }
  .sheet {
    position: relative;
    width: 1200px;
    height: 759px;
    background: var(--paper);
    overflow: hidden;
  }
  .side-label {
    position: absolute;
    top: 28px;
    width: 200px;
    margin-left: -100px;
    text-align: center;
    font-family: "Arimo", Helvetica, Arial, sans-serif;
    font-size: 29px;
    color: var(--ink);
    letter-spacing: 0.5px;
  }
  .side-label--front { left: 307px; }
  .side-label--back { left: 880px; }

  .card {
    position: absolute;
    width: 503px;
    height: 287px;
    box-sizing: border-box;
    overflow: hidden;
  }
  .card--front {
    border: 2px solid var(--ink);
    background: var(--paper);
  }
  .card--chairman { left: 51px; top: 87px; }
  .card--coo { left: 51px; top: 408px; }

  .card__watermark {
    position: absolute;
    left: 4px;
    top: 22px;
    width: 330px;
    height: 265px;
    background: radial-gradient(ellipse at 35% 55%, var(--watermark) 0%, rgba(236,236,236,0.55) 45%, rgba(255,255,255,0) 75%);
  }
  .card__band {
    position: absolute;
    left: 0;
    top: 20px;
    width: 100%;
    height: 78px;
    background: linear-gradient(to right, var(--band-light) 0%, rgba(255,255,255,0.6) 12%, #c9c3bf 45%, var(--band-dark) 100%);
  }
  .card__company {
    position: absolute;
    left: 28px;
    top: 44px;
    width: 150px;
    text-align: center;
    font-family: "Cinzel", "Times New Roman", serif;
    font-size: 12px;
    line-height: 14px;
    color: #6b5d56;
    letter-spacing: 0.3px;
  }
  .card__name {
    position: absolute;
    right: 34px;
    top: 36px;
    font-family: "Cinzel", "Times New Roman", serif;
    font-size: 19px;
    color: #ffffff;
    letter-spacing: 1.5px;
    white-space: nowrap;
  }
  .card__role {
    position: absolute;
    right: 34px;
    top: 62px;
    font-family: "Cormorant Garamond", Georgia, serif;
    font-style: italic;
    font-size: 17px;
    color: #ffffff;
    letter-spacing: 0.5px;
  }
  .card__contact {
    position: absolute;
    right: 34px;
    top: 208px;
    text-align: right;
    font-family: "Arimo", Helvetica, Arial, sans-serif;
    font-size: 16px;
    line-height: 22px;
    color: var(--ink);
  }

  .card--back {
    left: 629px;
    top: 88px;
    width: 502px;
    height: 286px;
    background: var(--brand-brown);
  }
  .card__wordmark {
    position: absolute;
    left: 0;
    top: 134px;
    width: 100%;
    text-align: center;
    font-family: "Cinzel", "Times New Roman", serif;
    color: #ffffff;
    font-size: 40px;
    line-height: 44px;
    letter-spacing: 1px;
  }
</style>
</head>
<body>
<main class="sheet">
  <div class="side-label side-label--front">FRONT</div>
  <div class="side-label side-label--back">BACK</div>

  <section class="card card--front card--chairman">
    <div class="card__watermark" role="img" aria-label="Faint ornamental scroll decoration"></div>
    <div class="card__band"></div>
    <div class="card__company">Solmaran Crest<br>Limited</div>
    <div class="card__name">Lasantha Wijeratne</div>
    <div class="card__role">Chairman</div>
    <div class="card__contact">
      Telephone: +94 11 2764502<br>
      Fax: +94 11 2764508
    </div>
  </section>

  <section class="card card--front card--coo">
    <div class="card__watermark" role="img" aria-label="Faint ornamental scroll decoration"></div>
    <div class="card__band"></div>
    <div class="card__company">Solmaran Crest<br>Limited</div>
    <div class="card__name">Nuwan S. Gunawardhana</div>
    <div class="card__role">COO</div>
    <div class="card__contact">
      Telephone: +94 11 2764502<br>
      Fax: +94 11 2764508
    </div>
  </section>

  <section class="card card--back">
    <div class="card__wordmark">Solmaran Crest<br>Limited</div>
  </section>
</main>
</body>
</html>
```